Hi all
We need an artistic, creative and modern business card design for our piano studio. Logo is attached, please let us know if you need other file formats.
The business card should convey high-end, prestigiousness, and be minimalist in feel. It should not look corporate or childish.
Rounded corners or creative shapes only, no regular square corners. Card should be double-sided. Can be portrait or landscape oriented. No preference to size either. Standard or custom size both okay.
We will not be giving out thousands of cards due to the nature of our business. We want to make sure that each business card we hand out, people will appreciate the design and printing quality that took place.
Please note, as the logo is supplied, we need more than just a layout with name and phone number etc inserted. Quite frankly,we can do that ourselves. We are interested in designs that has the different special printing methods in mind during the designing process. We are particularly interested in the effects of:
- Spot UV Varnish
- Foil
- Thermography
- Letterpress
- Die Cut
- Lamination
Colours does not have to be limited to black and white.
Information to be included:
Name (with qualification attached)
Mobile
website "talmer.com.au"
Designs submitted should include description of the printing method. The final format should be ready to be sent to printer with detailed printing method and colour (if applicable) instructions.
Much thanks in advance.
as per request from a designer, eps format file uploaded.

```html
<!DOCTYPE html>
<html lang="en">
<head>
<meta charset="utf-8">
<title>Talmer Piano Studio – Business Card, Version 1</title>
<link href="https://fonts.googleapis.com/css2?family=Questrial&family=Open+Sans:wght@400&family=Arimo:wght@400&display=swap" rel="stylesheet">
<style>
  :root {
    --wine: #8a0f24;
    --wine-deep: #6d0518;
    --wine-light: #9a1830;
    --ivory: #f4f1e8;
    --key-shade: #d9d6cc;
    --ink: #111111;
    --white: #ffffff;
    --header-top: #f4f4f4;
    --header-bottom: #e3e3e3;
    --clef-grey: #e6e6e6;
    --clef-red: #a2253a;
  }
  * { margin: 0; padding: 0; box-sizing: border-box; }
  html, body { width: 1200px; height: 900px; overflow: hidden; background: var(--white); }
  body { position: relative; font-family: "Questrial", sans-serif; color: var(--ink); }

  .sheet-header {
    position: absolute; left: 0; top: 0; width: 1200px; height: 68px;
    background: linear-gradient(var(--header-top), var(--header-bottom));
  }
  .sheet-header h1 {
    position: absolute; left: 33px; top: 16px;
    font-weight: 400; font-size: 34px; letter-spacing: 1px; line-height: 1;
  }
  .side-label {
    position: absolute; top: 84px; font-size: 31px; line-height: 1; letter-spacing: 1px;
    transform: translateX(-50%);
  }
  .side-label--front { left: 293px; }
  .side-label--back { left: 840px; }

  .card { position: absolute; overflow: hidden; }
  .card--front {
    left: 95px; top: 128px; width: 448px; height: 727px;
    border-radius: 0 80px 0 130px / 0 90px 0 170px;
    background: radial-gradient(ellipse at 40% 40%, var(--wine-light), var(--wine) 45%, var(--wine-deep));
  }
  .card--back {
    left: 636px; top: 130px; width: 450px; height: 730px;
    border-radius: 0 70px 0 130px / 0 90px 0 170px;
    background: var(--white);
    box-shadow: -3px 2px 6px rgba(0,0,0,0.12);
  }

  .keyboard {
    position: absolute; left: 0; top: 0; width: 100%;
    background: linear-gradient(180deg, #3a3f46 0%, #2a2e33 50%, var(--ivory) 51%, var(--ivory) 92%, var(--key-shade) 100%);
  }
  .card--front .keyboard { height: 134px; }
  .card--back .keyboard { height: 137px; }
  .keyboard-rail { position: absolute; left: 0; width: 100%; height: 16px; background: var(--ink); }
  .card--front .keyboard-rail { top: 134px; }
  .card--back .keyboard-rail { top: 137px; }

  .brand { position: absolute; font-family: "Questrial", sans-serif; font-weight: 400; }
  .brand-mark { display: block; }
  .brand-name { display: block; line-height: 1; }
  .brand-sub { display: block; line-height: 1; }

  .card--front .brand { left: 0; top: 257px; width: 100%; text-align: center; color: var(--white); }
  .card--front .brand-mark { width: 88px; height: 88px; margin: 0 auto 18px; background: var(--white); }
  .card--front .brand-name { font-size: 50px; letter-spacing: 14px; padding-left: 14px; }
  .card--front .brand-sub { font-size: 20px; letter-spacing: 6px; margin-top: 20px; padding-left: 6px; }

  .card--back .brand { left: 27px; top: 188px; color: var(--wine); display: flex; align-items: center; gap: 15px; }
  .card--back .brand-mark { width: 54px; height: 54px; background: var(--wine); }
  .card--back .brand-name { font-size: 36px; letter-spacing: 7px; }
  .card--back .brand-sub { font-size: 14px; letter-spacing: 4px; margin-top: 7px; }

  .clef { position: absolute; }
  .card--front .clef { left: 345px; top: 400px; width: 95px; height: 262px; }
  .card--back .clef { left: 19px; top: 345px; width: 100px; height: 265px; }

  .contact {
    position: absolute; right: 32px; top: 400px; text-align: right;
    font-family: "Open Sans", sans-serif; font-size: 19.5px; line-height: 29px; color: var(--ink);
  }
  .contact-name { color: var(--wine); font-size: 26px; line-height: 34px; }
  .contact-role { color: var(--wine); font-size: 19px; line-height: 24px; }

  .web {
    position: absolute; left: 0; width: 100%; text-align: center;
    font-family: "Arimo", sans-serif; color: var(--white);
  }
  .card--front .web { top: 664px; font-size: 27px; padding-left: 20px; }
  .web-band {
    position: absolute; left: 0; bottom: 0; width: 100%; height: 100px;
    background: linear-gradient(90deg, var(--wine-deep), var(--wine) 50%, var(--wine-deep));
  }
  .card--back .web { top: 30px; font-size: 24px; padding-left: 40px; }
</style>
</head>
<body>
  <header class="sheet-header"><h1>Version-1</h1></header>
  <p class="side-label side-label--front">Front</p>
  <p class="side-label side-label--back">Back</p>

  <section class="card card--front" aria-label="Card front">
    <div class="keyboard" role="img" aria-label="Piano keyboard illustration"></div>
    <div class="keyboard-rail"></div>
    <div class="brand">
      <span class="brand-mark"></span>
      <span class="brand-name">TALMER</span>
      <span class="brand-sub">PIANO STUDIO</span>
    </div>
    <svg class="clef" role="img" aria-label="Faint treble clef ornament" viewBox="0 0 95 262">
      <rect x="0" y="0" width="95" height="262" rx="40" fill="var(--clef-red)" opacity="0.25"/>
    </svg>
    <p class="web">www.talmer.com.au</p>
  </section>

  <section class="card card--back" aria-label="Card back">
    <div class="keyboard" role="img" aria-label="Piano keyboard illustration"></div>
    <div class="keyboard-rail"></div>
    <div class="brand">
      <span class="brand-mark"></span>
      <span>
        <span class="brand-name">TALMER</span>
        <span class="brand-sub">PIANO STUDIO</span>
      </span>
    </div>
    <svg class="clef" role="img" aria-label="Light grey treble clef ornament" viewBox="0 0 100 265">
      <rect x="0" y="0" width="100" height="265" rx="42" fill="var(--clef-grey)" opacity="0.8"/>
    </svg>
    <address class="contact" style="font-style: normal;">
      <div class="contact-name">Name</div>
      <div class="contact-role">Designation</div>
      <div>123,your street,your city</div>
      <div>your State-1234</div>
      <div>+123-456-789-000</div>
      <div>+000-987-654-321</div>
      <div>design@yourtext.com</div>
    </address>
    <div class="web-band"><p class="web">www.talmer.com.au</p></div>
  </section>
</body>
</html>
```